Advertising facade - tanning salon

We need outdoor advertising on the facade of the commercial property of a tanning salon. A stock photo from https://www.brontavel.example/de/social-media-units/k4r/ or https://media.vqt.example/europe-rest-of-world/aktuelle-solarien should / can -and-collarien / k4r-serie / can be used as a background.

The tanning salon logo is already available as an eps or svg file.

The background or the banner itself should be adapted to the facade of the property or give a coherent overall picture.

We need an outdoor advertisement on the facade of the commercial property of a tanning salon.

A stock photo from https://www.brontavel.example/de/social-media-units/k4r/ or https://media.vqt.example/europe-rest-of-world/aktuelle-solarien should / can -and-collarien / k4r-serie / can be used as a background.

The background or the banner should be adapted to the facade of the property or give a coherent overall picture.

Once a graphic is to be made on the commercial property from the outside (see annex outside) and a graphic for a print of a banner measuring 300x60cm.

The logo (see attachment Logo with background or gold frame) should be recognizable as the largest, preferably with a stock photo (see links above in the text) in all or part of the background.
The following should also be written on the logo:
Perfect tan? Now left
Un bronzage parfait? Maintenant à gauche

```html
<!DOCTYPE html>
<html lang="fr">
<head>
<meta charset="utf-8">
<title>Sonnenstudio Solvaria – Banner</title>
<link rel="stylesheet" href="https://fonts.googleapis.com/css2?family=Jost:wght@400&display=swap">
<style>
  :root {
    --page: #eeeeec;
    --banner: #4a4c45;
    --gold: #cfb46c;
    --bed-dark: #3a2a26;
    --bed-glow: #c86a3c;
    --bed-blue: #6fa7e0;
    --bed-pink: #d774b8;
    --bed-silver: #b9bcc2;
  }
  html, body {
    margin: 0;
    padding: 0;
    width: 1200px;
    height: 1135px;
    overflow: hidden;
    background: var(--page);
  }
  .canvas {
    position: relative;
    width: 1200px;
    height: 1135px;
  }
  .banner {
    position: absolute;
    left: 16px;
    top: 448px;
    width: 1168px;
    height: 238px;
    background: var(--banner);
    font-family: "Jost", sans-serif;
    font-weight: 400;
    color: var(--gold);
    overflow: hidden;
  }
  .banner__frame-outer,
  .banner__frame-inner {
    position: absolute;
    border: 1.5px solid var(--gold);
    pointer-events: none;
  }
  .banner__frame-outer { inset: 4px; }
  .banner__frame-inner { inset: 8px; border-width: 1px; }
  .brand-mark {
    position: absolute;
    left: 82px;
    top: 40px;
    width: 104px;
    height: 104px;
    border-radius: 50%;
    background: var(--gold);
  }
  .brand-name {
    margin: 0;
    font-weight: 400;
    white-space: nowrap;
    text-transform: uppercase;
    line-height: 1;
  }
  .brand-name__line1 {
    position: absolute;
    left: 262px;
    top: 22px;
    font-size: 74px;
    letter-spacing: 0.5px;
  }
  .brand-name__line2 {
    position: absolute;
    left: 305px;
    top: 102px;
    font-size: 58px;
    letter-spacing: 30px;
  }
  .divider {
    position: absolute;
    left: 18px;
    top: 167px;
    width: 838px;
    height: 0;
    border-top: 1px solid var(--gold);
  }
  .tagline {
    position: absolute;
    left: 44px;
    top: 173px;
    margin: 0;
    font-size: 42px;
    line-height: 1;
    white-space: nowrap;
  }
  .product-photo {
    position: absolute;
    left: 908px;
    top: 17px;
    width: 245px;
    height: 208px;
    border-radius: 16px 16px 8px 8px;
    background: linear-gradient(180deg,
      var(--bed-dark) 0%,
      var(--bed-silver) 16%,
      var(--bed-blue) 30%,
      var(--bed-pink) 42%,
      var(--bed-blue) 56%,
      var(--bed-glow) 78%,
      var(--bed-dark) 100%);
  }
</style>
</head>
<body>
<main class="canvas">
  <section class="banner">
    <div class="banner__frame-outer"></div>
    <div class="banner__frame-inner"></div>
    <div class="brand-mark"></div>
    <h1 class="brand-name">
      <span class="brand-name__line1">Sonnenstudio</span>
      <span class="brand-name__line2">Solvaria</span>
    </h1>
    <div class="divider"></div>
    <p class="tagline">Un bronzage parfait? Maintenant à gauche</p>
    <div class="product-photo" role="img" aria-label="Photo of an open tanning bed with glowing blue and pink lamps"></div>
  </section>
</main>
</body>
</html>
```